Marbury Church Winter Cantata 2013

Create a 18x22 inch poster for an upcoming church concert event with the following details:
Theme: Jesus Is Coming Again
Date:12/21/13 Time: 10:40am
Featuring the Choirs of the Marbury Church and special guests.
Marbury FBC Church
514-36 92nd Street,
Laurelton, NY 11287
Pastor Delton K. Fairweather
The target audience is predominantly african-american
The concert theme has been changed to: "Jesus The Light of the World"
Church

```html
<!DOCTYPE html>
<html lang="en">
<head>
<meta charset="utf-8">
<title>Jesus The Light of the World — Church Concert</title>
<link href="https://fonts.googleapis.com/css2?family=Tenor+Sans&family=Tinos&family=Courier+Prime:wght@700&family=Stardos+Stencil:wght@700&display=swap" rel="stylesheet">
<style>
  :root {
    --sky-light: #bfe6f7;
    --sky: #8fd0ef;
    --sky-deep: #5fb6e3;
    --flame: #f26a2a;
    --sun: #f7b21c;
    --paper: #ffffff;
    --ink: #111111;
    --wine: #a3141c;
  }
  html, body { margin: 0; padding: 0; overflow: hidden; background: #fff; }
  .poster {
    position: relative;
    width: 843px;
    height: 1200px;
    overflow: hidden;
    background:
      radial-gradient(ellipse 60% 30% at 70% 20%, rgba(255,255,255,.45), transparent 70%),
      radial-gradient(ellipse 50% 40% at 20% 55%, rgba(255,255,255,.35), transparent 70%),
      linear-gradient(160deg, var(--sky-light) 0%, var(--sky) 45%, var(--sky-deep) 75%, var(--sky) 100%);
  }
  .ground { position: absolute; left: 0; top: 0; }
  .performer {
    position: absolute;
    left: 178px;
    top: 570px;
    width: 290px;
    height: 500px;
    border-radius: 40% 40% 10% 10%;
    background: radial-gradient(ellipse at 50% 40%, rgba(120,120,110,.5), rgba(143,208,239,0) 70%);
  }
  .theme {
    position: absolute;
    top: 36px;
    left: 0;
    width: 843px;
    margin: 0;
    text-align: center;
    font-family: "Tenor Sans", sans-serif;
    font-weight: 400;
    font-size: 96px;
    line-height: 116px;
    color: var(--flame);
  }
  .theme .line { display: block; white-space: nowrap; }
  .theme .initial { color: var(--paper); }
  .details {
    position: absolute;
    left: 459px;
    top: 668px;
    width: 420px;
    transform: rotate(-15deg);
    transform-origin: left top;
    color: var(--wine);
    white-space: nowrap;
  }
  .details .when {
    margin: 0;
    font-family: "Tinos", serif;
    font-size: 36px;
    line-height: 42px;
  }
  .details .when .row { display: block; }
  .details .when .time { padding-left: 41px; }
  .details .where {
    margin: 30px 0 0 0;
    font-family: "Courier Prime", monospace;
    font-weight: 700;
    font-size: 22px;
    line-height: 31px;
  }
  .details .where .row { display: block; }
  .details .where .venue { padding-left: 10px; }
  .details .where .street { margin-left: -100px; }
  .details .where .city { padding-left: 38px; }
  .details .where .pastor { padding-left: 8px; }
  .event-type {
    position: absolute;
    left: 196px;
    top: 1118px;
    margin: 0;
    transform: rotate(-5.4deg);
    transform-origin: left top;
    font-family: "Stardos Stencil", sans-serif;
    font-weight: 700;
    font-size: 64px;
    line-height: 1;
    letter-spacing: 1px;
    color: var(--ink);
    white-space: nowrap;
  }
</style>
</head>
<body>
<main class="poster">
  <svg class="ground" width="843" height="1200" viewBox="0 0 843 1200">
    <defs>
      <linearGradient id="blaze" x1="0" y1="0" x2="1" y2="1">
        <stop offset="0" stop-color="#f7d23a"/>
        <stop offset=".45" stop-color="#f7b21c"/>
        <stop offset="1" stop-color="#f26a2a"/>
      </linearGradient>
    </defs>
    <path d="M0 930 C200 960 420 920 843 960 L843 1066 L0 1165 Z" fill="url(#blaze)" role="img" aria-label="Sunlit orange field with paint splatter texture"/>
    <path d="M0 1040 C260 1030 520 1000 843 990 L843 1066 L0 1165 Z" fill="#f26a2a" opacity=".7"/>
    <polygon points="0,1165 843,1066 843,1200 0,1200" fill="#ffffff"/>
  </svg>

  <div class="performer" role="img" aria-label="Photo of a young man seen from behind, raising a fist and holding an electric guitar"></div>

  <h1 class="theme">
    <span class="line"><span class="initial">J</span>ESUS</span>
    <span class="line"><span class="initial">T</span>HE <span class="initial">L</span>IGHT</span>
    <span class="line"><span class="initial">O</span>F THE</span>
    <span class="line"><span class="initial">W</span>ORLD</span>
  </h1>

  <div class="details">
    <p class="when"><span class="row">21 dec 2013</span><span class="row time">10:40am</span></p>
    <p class="where">
      <span class="row venue">Marbury FBC Church</span>
      <span class="row street">514-36 92nd Street, Laurelton,</span>
      <span class="row city">NY 11287 Pastor</span>
      <span class="row pastor">Delton K. Fairweather</span>
    </p>
  </div>

  <p class="event-type">CHURCH CONCERT</p>
</main>
</body>
</html>
```